Quiet Harbor Podcast Business Card Design

Needing a business card with the logo design provided for Quiet Harbor Podcast. I am looking for a modern style that fits the current logo.

Info:
Name: Teodor Vask
Title: Creator/Host
Email: teodor@quietharborcast.com
Phone: (555) 274-9163
www.quietharborcast.com
Twitter: @qharborcast
Instagram: @quietharborcastshow
Facebook: Quiet Harbor Podcast

Industry/Entity Type

Business

Font styles to use
Sans Serif

Colors
000000
ffffff

Requirements
Must have
• modern, clean design
Nice to have
• social media contact info

```html
<!DOCTYPE html>
<html lang="en">
<head>
<meta charset="utf-8">
<title>Quiet Harbor Podcast – Business Card</title>
<link rel="stylesheet" href="https://fonts.googleapis.com/css2?family=Montserrat:wght@700&family=Questrial&display=swap">
<style>
  :root {
    --ink: #000000;
    --paper: #ffffff;
    --card-face: #f2f2f0;
    --backdrop: #d9d6d2;
    --soft-ink: #1e1e1e;
  }
  html, body {
    margin: 0;
    width: 1200px;
    height: 969px;
    overflow: hidden;
    background: var(--backdrop);
  }
  .stage {
    position: relative;
    width: 1200px;
    height: 969px;
  }
  .business-card {
    position: absolute;
    left: 400px;
    top: 135px;
    width: 400px;
    height: 700px;
    box-sizing: border-box;
    background: var(--card-face);
    border: 8px solid var(--ink);
    display: flex;
    flex-direction: column;
    align-items: center;
    color: var(--soft-ink);
    font-family: "Questrial", sans-serif;
  }
  .brand {
    margin-top: 62px;
    display: flex;
    flex-direction: column;
    align-items: center;
    gap: 18px;
  }
  .brand-mark {
    width: 22px;
    height: 22px;
    background: var(--ink);
  }
  .brand-name {
    font-family: "Montserrat", sans-serif;
    font-weight: 700;
    font-size: 26px;
    letter-spacing: 0.5px;
    text-transform: uppercase;
    color: var(--ink);
    margin: 0;
  }
  .contact-list {
    list-style: none;
    margin: 26px 0 0;
    padding: 0;
    display: flex;
    flex-direction: column;
    align-items: center;
  }
  .contact-item {
    display: flex;
    flex-direction: column;
    align-items: center;
    margin-bottom: 13px;
  }
  .icon-rule {
    display: flex;
    align-items: center;
    gap: 8px;
    margin-bottom: 6px;
  }
  .icon-rule::before,
  .icon-rule::after {
    content: "";
    width: 40px;
    height: 2px;
    background: var(--ink);
  }
  .icon-badge {
    width: 26px;
    height: 26px;
    display: block;
  }
  .person-name {
    font-family: "Montserrat", sans-serif;
    font-weight: 700;
    font-size: 26px;
    letter-spacing: 0.5px;
    text-transform: uppercase;
    color: var(--ink);
    line-height: 1.1;
  }
  .person-title {
    font-size: 18px;
    color: var(--ink);
    line-height: 1.2;
  }
  .contact-text {
    font-size: 16px;
    line-height: 1.2;
  }
</style>
</head>
<body>
<main class="stage">
  <article class="business-card">
    <header class="brand">
      <span class="brand-mark" aria-hidden="true"></span>
      <h1 class="brand-name">Quiet Harbor Podcast</h1>
    </header>

    <ul class="contact-list">
      <li class="contact-item">
        <span class="icon-rule">
          <svg class="icon-badge" viewBox="0 0 26 26" aria-hidden="true">
            <circle cx="13" cy="13" r="13" fill="var(--ink)"/>
            <circle cx="13" cy="10" r="3.6" fill="var(--paper)"/>
            <path d="M6.5 19.5c0-3.6 2.9-5.6 6.5-5.6s6.5 2 6.5 5.6z" fill="var(--paper)"/>
          </svg>
        </span>
        <span class="person-name">Teodor Vask</span>
        <span class="person-title">Creator/Host</span>
      </li>

      <li class="contact-item">
        <span class="icon-rule">
          <svg class="icon-badge" viewBox="0 0 26 26" aria-hidden="true">
            <circle cx="13" cy="13" r="13" fill="var(--ink)"/>
            <path d="M9 7.5l2.2 2.6-1.3 1.6c.8 1.8 2.2 3.2 4 4l1.6-1.3 2.6 2.2-1.4 1.9c-4.6-.4-8.6-4.4-9-9z" fill="var(--paper)"/>
          </svg>
        </span>
        <span class="contact-text">(555) 274-9163</span>
      </li>

      <li class="contact-item">
        <span class="icon-rule">
          <svg class="icon-badge" viewBox="0 0 26 26" aria-hidden="true">
            <circle cx="13" cy="13" r="13" fill="var(--ink)"/>
            <rect x="7" y="8.5" width="12" height="9" fill="var(--paper)"/>
            <path d="M7 8.5l6 5 6-5" fill="none" stroke="var(--ink)" stroke-width="1.2"/>
          </svg>
        </span>
        <span class="contact-text">teodor@quietharborcast.com</span>
      </li>

      <li class="contact-item">
        <span class="icon-rule">
          <svg class="icon-badge" viewBox="0 0 26 26" aria-hidden="true">
            <circle cx="13" cy="13" r="13" fill="var(--ink)"/>
            <circle cx="13" cy="13" r="6.5" fill="none" stroke="var(--paper)" stroke-width="1.4"/>
            <ellipse cx="13" cy="13" rx="2.8" ry="6.5" fill="none" stroke="var(--paper)" stroke-width="1.2"/>
            <line x1="6.5" y1="13" x2="19.5" y2="13" stroke="var(--paper)" stroke-width="1.2"/>
          </svg>
        </span>
        <span class="contact-text">www.quietharborcast.com</span>
      </li>

      <li class="contact-item">
        <span class="icon-rule">
          <svg class="icon-badge" viewBox="0 0 26 26" aria-hidden="true">
            <circle cx="13" cy="13" r="13" fill="var(--ink)"/>
          </svg>
        </span>
        <span class="contact-text">Quiet Harbor Podcast</span>
      </li>

      <li class="contact-item">
        <span class="icon-rule">
          <svg class="icon-badge" viewBox="0 0 26 26" aria-hidden="true">
            <circle cx="13" cy="13" r="13" fill="var(--ink)"/>
          </svg>
        </span>
        <span class="contact-text">@quietharborcastshow</span>
      </li>

      <li class="contact-item">
        <span class="icon-rule">
          <svg class="icon-badge" viewBox="0 0 26 26" aria-hidden="true">
            <circle cx="13" cy="13" r="13" fill="var(--ink)"/>
          </svg>
        </span>
        <span class="contact-text">@qharborcast</span>
      </li>
    </ul>
  </article>
</main>
</body>
</html>
```